Private Investigation Business Card Design

I need a business card for a new private investigation company named Brisk Lens Inquiries. I perform mainly surveillance jobs, vehicle repossessions, document serves etc. The final design should aim for a professional look. The logo has a magnifying glass with stick man arms and legs and is in a running action to show the "BRISK" aspect of the name. If the colour scheme could remain the same as the website www.brisklensinquiries.example.au with silvers,blacks and a couple electric blue highlights.
Industry/Entity Type
Business
Contact Information for Business Card
Morgan Kilbride
Brisk Lens Inquiries
0438276104
PO Box 58, Fernvale NSW 2291
info@brisklensinquiries.example.au
www.brisklensinquiries.example.au
Look and feel
Each slider illustrates characteristics of the customer's brand and the style your logo design should communicate.

```html
<!DOCTYPE html>
<html lang="en">
<head>
<meta charset="utf-8">
<title>Brisk Lens Inquiries – Business Card</title>
<link href="https://fonts.googleapis.com/css2?family=Lato:wght@400;700;900&display=swap" rel="stylesheet">
<style>
  :root {
    --backdrop: #e6e6e6;
    --card-white: #fbfbfb;
    --card-dark: #4a4b4f;
    --card-dark-edge: #3c3d41;
    --ink: #1d1d1f;
    --ink-soft: #333336;
    --silver: #9a9a9e;
    --silver-dark: #5e5f63;
    --silver-light: #c4c4c7;
    --brand-on-dark: #b9babd;
  }
  * { margin: 0; padding: 0; box-sizing: border-box; }
  html, body { width: 1200px; height: 720px; overflow: hidden; }
  body {
    background: var(--backdrop);
    font-family: "Lato", Arial, sans-serif;
    position: relative;
  }
  .card {
    position: absolute;
    top: 242px;
    width: 420px;
    height: 238px;
    border-radius: 8px;
    overflow: hidden;
  }
  .card-front { left: 148px; background: var(--card-white); }
  .card-back {
    left: 633px;
    background: linear-gradient(160deg, var(--card-dark) 0%, var(--card-dark-edge) 100%);
  }
  .swoosh { position: absolute; inset: 0; }
  .brand {
    position: absolute;
    display: flex;
    align-items: center;
    gap: 8px;
    font-weight: 900;
    letter-spacing: 0.5px;
    white-space: nowrap;
  }
  .brand-mark {
    width: 16px; height: 16px;
    border-radius: 50%;
    flex: none;
  }
  .card-front .brand {
    top: 28px; right: 26px;
    font-size: 22px;
    color: var(--silver-dark);
  }
  .card-front .brand-mark { background: var(--silver); }
  .card-back .brand {
    top: 50%; left: 50%;
    transform: translate(-50%, -50%);
    font-size: 28px;
    color: var(--brand-on-dark);
  }
  .card-back .brand-mark { background: var(--brand-on-dark); width: 18px; height: 18px; }
  .holder { position: absolute; left: 20px; top: 124px; }
  .holder-name { font-size: 17px; font-weight: 700; color: var(--ink); }
  .holder-role { font-size: 12px; color: var(--ink-soft); margin-top: 1px; }
  .contacts {
    position: absolute; left: 20px; top: 177px;
    list-style: none;
    font-size: 11px; color: var(--ink); line-height: 14px;
  }
  .contacts li { display: flex; align-items: center; gap: 5px; }
  .contacts svg { width: 11px; height: 10px; flex: none; fill: var(--ink); }
  .address {
    position: absolute; right: 68px; top: 191px;
    font-size: 11px; line-height: 14px; color: var(--ink);
    text-align: right; font-style: normal;
  }
</style>
</head>
<body>
  <section class="card card-front" aria-label="Card front">
    <svg class="swoosh" viewBox="0 0 420 238" aria-hidden="true">
      <path d="M0,58 Q255,46 414,238 Q250,80 0,78 Z" fill="#6a6b6f"/>
      <path d="M0,80 Q250,82 414,238 Q240,102 0,94 Z" fill="#b6b7ba"/>
    </svg>
    <div class="brand"><span class="brand-name">Brisk Lens Inquiries</span><span class="brand-mark"></span></div>
    <div class="holder">
      <div class="holder-name">Morgan Kilbride</div>
      <div class="holder-role">Director</div>
    </div>
    <ul class="contacts">
      <li><svg viewBox="0 0 12 10"><path d="M1,3 Q6,-1 11,3 L10,5 L8,4 L8,3 Q6,2 4,3 L4,4 L2,5 Z M3,5 L9,5 L10,9 L2,9 Z"/></svg>0438276104</li>
      <li><svg viewBox="0 0 12 10"><path d="M0,0 H12 V10 H0 Z M1,1.5 V2.2 L6,5.5 L11,2.2 V1.5 L6,4.6 Z" fill-rule="evenodd"/></svg>info@brisklensinquiries.example.au</li>
      <li><svg viewBox="0 0 12 10"><path d="M0,0 H12 V7.5 H7 V9 H9 V10 H3 V9 H5 V7.5 H0 Z M1,1 V6.5 H11 V1 Z" fill-rule="evenodd"/></svg>www.brisklensinquiries.example.au</li>
    </ul>
    <address class="address">PO Box 58<br>Fernvale NSW 2291</address>
  </section>

  <section class="card card-back" aria-label="Card back">
    <div class="brand"><span class="brand-name">Brisk Lens Inquiries</span><span class="brand-mark"></span></div>
  </section>
</body>
</html>
```